Business Card Design Project

New business card design front and back for IT company that does network support and web design.
Calloway IT
Doug Calloway
Managing Director
PO Box 918 Brinsley VIC 3421
doug@callowayit.example
www.callowayit.example

Industry/Entity Type

Business

```html
<!DOCTYPE html>
<html lang="en">
<head>
<meta charset="utf-8">
<title>Calloway IT – Business Card</title>
<link href="https://fonts.googleapis.com/css2?family=Exo+2:wght@300;400&display=swap" rel="stylesheet">
<style>
  :root {
    --navy-deep: #16304f;
    --navy-mid: #2c5a88;
    --steel-blue: #3f76a4;
    --title-blue: #93abd3;
    --tagline-blue: #c4d3ea;
    --contact-grey: #a9bdd6;
    --icon-grey: #8c96a2;
    --card-grey: #d9d9d9;
    --back-navy: #002d52;
    --text-dark: #333333;
    --white: #ffffff;
  }
  html, body {
    margin: 0;
    padding: 0;
    width: 1000px;
    height: 1200px;
    overflow: hidden;
    background: var(--card-grey);
  }
  .card {
    position: relative;
    width: 1000px;
    height: 1200px;
    font-family: "Exo 2", sans-serif;
    overflow: hidden;
  }
  /* Front side */
  .card-front {
    position: absolute;
    left: 0; top: 0;
    width: 1000px;
    height: 600px;
    background: linear-gradient(to bottom, var(--navy-deep) 0%, var(--navy-mid) 50%, var(--steel-blue) 100%);
  }
  .brand-title {
    position: absolute;
    left: 0; right: 0;
    top: 48px;
    margin: 0;
    text-align: center;
    font-weight: 400;
    font-size: 112px;
    line-height: 1;
    color: var(--title-blue);
    letter-spacing: 1px;
  }
  .title-rule {
    position: absolute;
    left: 55px;
    width: 890px;
    top: 176px;
    height: 4px;
    background: linear-gradient(to right, rgba(147,171,211,0) 0%, var(--title-blue) 30%, var(--title-blue) 70%, rgba(147,171,211,0) 100%);
  }
  .front-tagline {
    position: absolute;
    left: 0; right: 0;
    top: 199px;
    text-align: center;
    font-size: 20px;
    color: var(--tagline-blue);
    letter-spacing: 1px;
  }
  .brand-mark {
    position: absolute;
    display: flex;
    align-items: center;
    gap: 12px;
    font-size: 30px;
    font-weight: 400;
  }
  .brand-mark-front {
    left: 0; right: 0;
    top: 272px;
    justify-content: center;
    color: var(--title-blue);
  }
  .brand-mark-dot {
    width: 18px;
    height: 18px;
    border-radius: 50%;
    background: currentColor;
  }
  .contact-item {
    position: absolute;
    top: 490px;
    display: flex;
    align-items: center;
    gap: 14px;
    font-size: 28px;
    color: var(--contact-grey);
  }
  .contact-phone { left: 55px; }
  .contact-web { left: 582px; }
  .contact-icon { width: 70px; height: 70px; }

  /* Back side */
  .card-back {
    position: absolute;
    left: 0; top: 600px;
    width: 1000px;
    height: 600px;
    background: var(--card-grey);
  }
  .back-wedge {
    position: absolute;
    left: 0; top: 0;
    width: 1000px;
    height: 600px;
  }
  .contact-details {
    position: absolute;
    left: 43px;
    top: 84px;
    margin: 0;
    font-style: normal;
    font-size: 28px;
    line-height: 36px;
    color: var(--text-dark);
  }
  .brand-mark-back {
    left: 600px;
    top: 462px;
    color: var(--white);
  }
  .back-tagline {
    position: absolute;
    right: 12px;
    top: 535px;
    font-size: 45px;
    font-weight: 300;
    color: var(--white);
    letter-spacing: 2px;
    white-space: nowrap;
  }
</style>
</head>
<body>
<main class="card">
  <section class="card-front">
    <h1 class="brand-title">Calloway IT</h1>
    <div class="title-rule"></div>
    <div class="front-tagline">IT Solutions For Your Business</div>
    <div class="brand-mark brand-mark-front"><span class="brand-mark-dot"></span><span>Calloway IT</span></div>

    <div class="contact-item contact-phone">
      <svg class="contact-icon" viewBox="0 0 70 70" aria-hidden="true">
        <path d="M14 8 L24 6 L30 20 L23 26 C27 36 33 43 43 48 L49 41 L63 47 L61 58 C58 63 52 64 46 62 C30 55 17 42 9 25 C7 18 9 12 14 8 Z" fill="var(--icon-grey)"/>
      </svg>
      <span>0455 218 604</span>
    </div>

    <div class="contact-item contact-web">
      <svg class="contact-icon" viewBox="0 0 70 70" aria-hidden="true">
        <circle cx="35" cy="35" r="30" fill="none" stroke="var(--icon-grey)" stroke-width="5"/>
        <ellipse cx="35" cy="35" rx="13" ry="30" fill="none" stroke="var(--icon-grey)" stroke-width="4"/>
        <line x1="35" y1="5" x2="35" y2="65" stroke="var(--icon-grey)" stroke-width="4"/>
        <line x1="5" y1="35" x2="65" y2="35" stroke="var(--icon-grey)" stroke-width="4"/>
        <line x1="10" y1="20" x2="60" y2="20" stroke="var(--icon-grey)" stroke-width="4"/>
        <line x1="10" y1="50" x2="60" y2="50" stroke="var(--icon-grey)" stroke-width="4"/>
      </svg>
      <span>www.callowayit.example</span>
    </div>
  </section>

  <section class="card-back">
    <svg class="back-wedge" viewBox="0 0 1000 600" aria-hidden="true">
      <polygon points="1000,0 1000,600 0,600" fill="var(--back-navy)"/>
    </svg>
    <address class="contact-details">
      Doug Calloway<br>
      Managing Director<br>
      PO Box 918 Brinsley VIC 3421<br>
      0455 218 604<br>
      doug@callowayit.example<br>
      www.callowayit.example
    </address>
    <div class="brand-mark brand-mark-back"><span class="brand-mark-dot"></span><span>Calloway IT</span></div>
    <div class="back-tagline">IT Solutions For Your Business</div>
  </section>
</main>
</body>
</html>
```